Business card design needed

I am a local business in the Blue Mountains area of Sydney. I am a sole trader and the business has been operating 7 months. To date the business has been built on referrals only and all my clinets for both home & commercial services are themselves business owners. I specialise in Home and Office cleaning and small business cleaning for example cafes, restuarants, health clinics.
I would like a clean looking design( maybe a white background). If its possible(not madatory) to incorporate a duster, or mop & bucket into the design or roof tops to communicate business premises that would be great. I would like my clients to know what the business is from the card. My uniform is navy with red/pink logo on .Attatched is the unifrom logo but it is not critical to match the font for the business card.
please put my name on contact details; Carol Whitby, Business owner.
Updates
Thank you very much to all the designers and their work efforts to submit a design for Bright Feather Domestic Services. I have made a decision to accept the deign that Velo Design of the United States submitted. Again Many thanks. Carol
Target Market(s)
business owners, generally women between 35-55
Industry/Entity Type
Small Business
Contact Information for Business Card
Bright Feather Domestic Services,
specialist in Home & Small business cleaning
Lithgow NSW
tel: 0491570156 0491tidyup
Logo Text
Bright Feather Domestic Servies
Logo styles of interest
Emblem Logo
Abstract Logo
Wordmark Logo
Look and feel

```html
<!DOCTYPE html>
<html lang="en">
<head>
<meta charset="utf-8">
<title>Bright Feather Domestic Services – Business Card</title>
<link rel="stylesheet" href="https://fonts.googleapis.com/css2?family=Didact+Gothic&family=Rokkitt:wght@700&display=swap">
<style>
  :root {
    --card-bg: #ffffff;
    --ink: #111111;
    --broom-tone: #4a90d9;
    --broom-head: #f2d23a;
    --bucket-tone: #3c6b5a;
    --supplies-tone: #d9487e;
    --mop-tone: #e6dccb;
    --glove-tone: #f5c518;
  }
  html, body {
    margin: 0;
    padding: 0;
    overflow: hidden;
    background: var(--card-bg);
  }
  .card {
    position: relative;
    width: 1200px;
    height: 693px;
    background: var(--card-bg);
    overflow: hidden;
    color: var(--ink);
  }
  .card__line {
    position: absolute;
    left: 0;
    width: 100%;
    margin: 0;
    text-align: center;
    white-space: nowrap;
    line-height: 1;
  }
  .owner-name {
    top: 116px;
    font-family: "Didact Gothic", sans-serif;
    font-variant: small-caps;
    font-size: 70px;
    letter-spacing: 2px;
    font-weight: 400;
  }
  .business-name {
    top: 196px;
    font-family: "Rokkitt", serif;
    font-weight: 700;
    font-size: 60px;
    letter-spacing: 1px;
  }
  .tagline {
    top: 258px;
    font-family: "Didact Gothic", sans-serif;
    font-variant: small-caps;
    font-size: 48px;
    letter-spacing: 1px;
  }
  .location {
    top: 305px;
    font-family: "Didact Gothic", sans-serif;
    font-variant: small-caps;
    font-size: 52px;
    letter-spacing: 1px;
  }
  .phone {
    top: 362px;
    font-family: "Didact Gothic", sans-serif;
    font-variant: small-caps;
    font-size: 50px;
    letter-spacing: 1px;
  }
  .artwork {
    position: absolute;
  }
  .artwork--broom { left: 0; top: 423px; width: 195px; height: 270px; }
  .artwork--bucket { left: 429px; top: 469px; width: 330px; height: 224px; }
  .artwork--mop { left: 1022px; top: 423px; width: 178px; height: 270px; }
</style>
</head>
<body>
<main class="card">
  <h1 class="card__line owner-name">Carol Whitby</h1>
  <h2 class="card__line business-name">Bright Feather Domestic Services</h2>
  <p class="card__line tagline">specialist in home &amp; small business cleaning</p>
  <p class="card__line location">Lithgow NSW</p>
  <p class="card__line phone">tel: 0491 tidy up (0491570156)</p>

  <svg class="artwork artwork--broom" viewBox="0 0 195 270" role="img" aria-label="Photo of a gloved hand holding a blue broom with a yellow head">
    <defs>
      <linearGradient id="broomFill" x1="0" y1="0" x2="0" y2="1">
        <stop offset="0" stop-color="var(--broom-head)"/>
        <stop offset="0.35" stop-color="var(--broom-tone)"/>
        <stop offset="1" stop-color="var(--glove-tone)"/>
      </linearGradient>
    </defs>
    <rect x="0" y="0" width="195" height="270" rx="18" fill="url(#broomFill)" opacity="0.55"/>
  </svg>

  <svg class="artwork artwork--bucket" viewBox="0 0 330 224" role="img" aria-label="Photo of a green bucket filled with cleaning sprays, sponges and gloves">
    <defs>
      <linearGradient id="bucketFill" x1="0" y1="0" x2="0" y2="1">
        <stop offset="0" stop-color="var(--supplies-tone)"/>
        <stop offset="0.45" stop-color="var(--bucket-tone)"/>
        <stop offset="1" stop-color="var(--broom-tone)"/>
      </linearGradient>
    </defs>
    <rect x="0" y="0" width="330" height="224" rx="22" fill="url(#bucketFill)" opacity="0.6"/>
  </svg>

  <svg class="artwork artwork--mop" viewBox="0 0 178 270" role="img" aria-label="Photo of a gloved hand holding a white string mop">
    <defs>
      <linearGradient id="mopFill" x1="0" y1="0" x2="0" y2="1">
        <stop offset="0" stop-color="var(--mop-tone)"/>
        <stop offset="0.6" stop-color="#c9c9c9"/>
        <stop offset="1" stop-color="var(--glove-tone)"/>
      </linearGradient>
    </defs>
    <rect x="0" y="0" width="178" height="270" rx="18" fill="url(#mopFill)" opacity="0.7"/>
  </svg>
</main>
</body>
</html>
```